Copper Lantern ebook cover

We need a book cover design for new book: The Copper Lantern: The Quiet Drive, Choices, and Rituals That Will Set You Free! By Dorian Pelkey. We have 2 different ideas for the cover that we want to see executed.
#1 is Copper Lantern bold and at the top with a $ symbol in the center with clean smaller icons surrounding it in a hexagon shape:
bed
smoothie/juice
running /workout (lifting/running)
gratitude journal/writing
book
meditation
We're inspired by books like this: http://brivoltpress.com/wp-content/uploads/2016/03/the-ledger-3d-163x300.png although we do not want to use gold/foil for print.
#2 idea is just clean large bold text with inspiring background. Inspirational ideas: http://quennardgroup.com/wp-content/uploads/2014/08/4BookVantagePackageQuennard.jpg
Entrepreneur

```html
<!DOCTYPE html>
<html lang="en">
<head>
<meta charset="utf-8">
<title>The Copper Lantern — Dorian Pelkey</title>
<link href="https://fonts.googleapis.com/css2?family=Bebas+Neue&display=swap" rel="stylesheet">
<style>
  :root {
    --cover-green: #2e8a51;
    --paper-white: #ffffff;
    --cash-light: #d9ded3;
    --cash-mid: #9fb39a;
    --cash-dark: #5f7a62;
  }
  html, body {
    margin: 0;
    padding: 0;
    width: 795px;
    height: 1200px;
    overflow: hidden;
    background: var(--paper-white);
  }
  .cover {
    position: relative;
    width: 795px;
    height: 1200px;
    overflow: hidden;
    background: var(--cover-green);
    font-family: "Bebas Neue", "Oswald", sans-serif;
    color: var(--paper-white);
  }
  .cover__art {
    position: absolute;
    inset: 0;
    width: 795px;
    height: 1200px;
  }
  .title {
    position: absolute;
    left: 0;
    right: 0;
    top: 196px;
    margin: 0;
    text-align: center;
    font-weight: 400;
    line-height: 1;
  }
  .title__article {
    display: block;
    font-size: 122px;
    letter-spacing: 1px;
  }
  .title__line {
    display: block;
    font-size: 128px;
    letter-spacing: 1px;
    margin-top: 6px;
  }
  .title__line--large {
    font-size: 214px;
    margin-top: -6px;
    letter-spacing: 2px;
  }
  .subtitle {
    position: absolute;
    left: 82px;
    top: 726px;
    margin: 0;
    font-size: 44px;
    line-height: 51px;
    font-weight: 400;
    letter-spacing: 0.5px;
  }
  .author {
    position: absolute;
    right: 0;
    top: 912px;
    display: flex;
    flex-direction: column;
    align-items: flex-end;
    gap: 18px;
    margin: 0;
    font-weight: 400;
  }
  .author__name {
    display: block;
    background: var(--paper-white);
    color: var(--cover-green);
    font-size: 146px;
    line-height: 122px;
    height: 122px;
    padding: 4px 10px 0 26px;
    letter-spacing: 1px;
  }
</style>
</head>
<body>
  <main class="cover">
    <svg class="cover__art" viewBox="0 0 795 1200" xmlns="http://www.w3.org/2000/svg">
      <defs>
        <linearGradient id="cash-top" x1="0" y1="0" x2="1" y2="1">
          <stop offset="0" stop-color="var(--cash-light)"/>
          <stop offset="0.5" stop-color="var(--cash-mid)"/>
          <stop offset="1" stop-color="var(--cash-dark)"/>
        </linearGradient>
        <linearGradient id="cash-bottom" x1="1" y1="0" x2="0" y2="1">
          <stop offset="0" stop-color="var(--cash-light)"/>
          <stop offset="0.5" stop-color="var(--cash-mid)"/>
          <stop offset="1" stop-color="var(--cash-dark)"/>
        </linearGradient>
      </defs>
      <g class="torn-edge">
        <polygon fill="var(--paper-white)" points="0,0 560,0 548,8 520,26 494,40 470,58 440,74 410,96 380,112 350,134 318,150 288,172 256,188 226,210 194,226 164,248 132,264 102,286 70,302 40,324 12,340 0,350 0,380"/>
        <polygon fill="var(--paper-white)" points="795,686 795,1200 0,1200 0,1132 24,1118 56,1096 86,1082 118,1060 150,1044 182,1022 212,1006 244,984 276,968 308,946 338,930 370,908 402,892 434,870 466,854 496,834 528,816 560,796 592,780 622,760 654,744 686,722 718,706 750,690 780,678"/>
      </g>
      <polygon class="cash-stack cash-stack--top" role="img" aria-label="Photograph of scattered bundles of hundred-dollar bills"
        fill="url(#cash-top)"
        points="0,0 552,0 540,10 512,28 486,44 462,60 432,78 402,98 372,116 342,136 310,154 280,174 248,192 218,212 186,230 156,250 124,268 94,288 62,306 32,326 6,342 0,346"/>
      <polygon class="cash-stack cash-stack--bottom" role="img" aria-label="Photograph of scattered bundles of hundred-dollar bills"
        fill="url(#cash-bottom)"
        points="795,694 795,1200 0,1200 0,1142 28,1124 60,1104 90,1088 122,1066 154,1050 186,1028 216,1012 248,990 280,974 312,952 342,936 374,914 406,898 438,876 470,860 500,840 532,822 564,802 596,786 626,766 658,750 690,728 722,712 754,696 784,684"/>
    </svg>

    <h1 class="title">
      <span class="title__article">The</span>
      <span class="title__line">Copper</span>
      <span class="title__line title__line--large">Lantern</span>
    </h1>

    <p class="subtitle">
      The Quiet Drive,<br>
      Choices, and Rituals<br>
      That Will Set You Free
    </p>

    <p class="author">
      <span class="author__name">Dorian</span>
      <span class="author__name">Pelkey</span>
    </p>
  </main>
</body>
</html>
```